The Licensing Sage
Business Cards and Stationary
The Licensing Sage -
Creative Brief
Use specific fonts
similar to my logo, the same may be too much
Cutting-Edge
Tessa Corvane
President
P.O. Box 518 Midway, Utah 84071
Tessa@TheLicensingSage.example
TheLicensingSage.example
Let us share the wisdom we have acquired from running franchises and selling hundreds of them. Our service is always free to you. (at bottom, in very small print) Member of the Outlet Compact

```html
<!DOCTYPE html>
<html lang="en">
<head>
<meta charset="utf-8">
<title>The Licensing Sage – Stationery</title>
<link href="https://fonts.googleapis.com/css2?family=Montserrat:wght@400;600;700&display=swap" rel="stylesheet">
<style>
:root{
  --backdrop:#e9e4dc;
  --paper:#ffffff;
  --green:#2f9a3a;
  --green-light:#7cc242;
  --green-dark:#1d7a2a;
  --orange:#f08a24;
  --ink:#555555;
  --rule:#c9c9c9;
  --label:#3b3b3b;
  --watermark:rgba(47,154,58,.07);
}
*{margin:0;padding:0;box-sizing:border-box}
html,body{width:1200px;height:562px;overflow:hidden;background:var(--backdrop);font-family:"Montserrat",sans-serif;color:var(--ink)}
.canvas{position:relative;width:1200px;height:562px}
.piece{position:absolute;background:var(--paper);box-shadow:0 2px 6px rgba(0,0,0,.25);overflow:hidden}
.piece-label{position:absolute;font-size:8px;font-weight:600;color:var(--label);text-align:center;width:100%;top:-13px;left:0}
.wrap{position:absolute}
.brand{font-weight:700;color:var(--green);white-space:nowrap;display:flex;align-items:center;gap:5px}
.brand .dot{display:inline-block;border-radius:50%;background:var(--orange);flex:none}
.wave{position:absolute;left:0;bottom:0;width:100%}
.footer-text{position:absolute;left:0;width:100%;text-align:center;color:#fff;font-size:5.5px;bottom:12px;white-space:nowrap}
.member-line{position:absolute;left:0;width:100%;text-align:center;color:#fff;font-size:4.5px;bottom:4px;white-space:nowrap}
.watermark-name{position:absolute;left:0;width:100%;text-align:center;font-weight:700;font-size:30px;color:var(--watermark);white-space:nowrap}
/* fax */
.fax-title{position:absolute;right:20px;top:75px;font-size:8px;font-weight:700;color:var(--label)}
.fax-table{position:absolute;left:20px;top:88px;width:320px;border-collapse:collapse;font-size:7px}
.fax-table td{border:1px solid var(--rule);height:17px;padding:0 5px;width:25%}
.fax-checks{position:absolute;left:20px;top:178px;width:320px;display:flex;justify-content:space-between;font-size:6.5px;white-space:nowrap}
.fax-checks span::before{content:"";display:inline-block;width:6px;height:6px;border:1px solid #888;margin-right:4px;vertical-align:-1px}
/* card */
.card-contact{position:absolute;right:10px;top:12px;text-align:right;font-size:5px;line-height:1.5}
.card-contact .name{font-weight:700;font-size:6px;color:var(--green-dark)}
.card-back{background:linear-gradient(160deg,var(--green-light),var(--green) 55%,var(--green-dark))}
.card-back p{position:absolute;left:14px;top:20px;width:110px;color:#fff;font-size:5.5px;line-height:1.5}
.tagline{font-size:5px;color:var(--ink)}
</style>
</head>
<body>
<div class="canvas">

  <!-- Fax cover -->
  <div class="wrap" style="left:24px;top:29px;width:360px;height:504px">
    <div class="piece-label">Fax Cover</div>
    <div class="piece" style="inset:0">
      <div class="brand" style="position:absolute;left:120px;top:22px;font-size:15px"><span class="dot" style="width:10px;height:10px"></span>The Licensing Sage</div>
      <div class="fax-title">FAX</div>
      <table class="fax-table">
        <tr><td>To:</td><td></td><td>From:</td><td></td></tr>
        <tr><td>Fax:</td><td></td><td>Pages:</td><td></td></tr>
        <tr><td>Phone:</td><td></td><td>Date:</td><td></td></tr>
        <tr><td>Re:</td><td></td><td>CC:</td><td></td></tr>
      </table>
      <div class="fax-checks"><span>Urgent</span><span>For Review</span><span>Please Comment</span><span>Please Reply</span><span>Please Recycle</span></div>
      <div class="watermark-name" style="top:330px">The Licensing Sage</div>
      <svg class="wave" width="360" height="60" viewBox="0 0 360 60" preserveAspectRatio="none">
        <path d="M0 22 Q180 0 360 18" fill="none" stroke="var(--orange)" stroke-width="2"/>
        <path d="M0 28 Q180 6 360 24 L360 60 L0 60Z" fill="var(--green)"/>
      </svg>
      <div class="footer-text">P.O. Box 518 Midway, Utah 84071 · Tel 801-555-0142 · Tessa@TheLicensingSage.example · TheLicensingSage.example</div>
      <div class="member-line">Member of the Outlet Compact</div>
    </div>
  </div>

  <!-- Letterhead -->
  <div class="wrap" style="left:408px;top:29px;width:360px;height:504px">
    <div class="piece-label">Letterhead</div>
    <div class="piece" style="inset:0">
      <div class="brand" style="position:absolute;left:120px;top:22px;font-size:15px"><span class="dot" style="width:10px;height:10px"></span>The Licensing Sage</div>
      <div class="watermark-name" style="top:330px">The Licensing Sage</div>
      <svg class="wave" width="360" height="60" viewBox="0 0 360 60" preserveAspectRatio="none">
        <path d="M0 22 Q180 0 360 18" fill="none" stroke="var(--orange)" stroke-width="2"/>
        <path d="M0 28 Q180 6 360 24 L360 60 L0 60Z" fill="var(--green)"/>
      </svg>
      <div class="footer-text">P.O. Box 518 Midway, Utah 84071 · Tel 801-555-0142 · Tessa@TheLicensingSage.example · TheLicensingSage.example</div>
      <div class="member-line">Member of the Outlet Compact</div>
    </div>
  </div>

  <!-- Business card front -->
  <div class="wrap" style="left:775px;top:29px;width:196px;height:103px">
    <div class="piece-label">Business Card (Front)</div>
    <div class="piece" style="inset:0">
      <div class="brand" style="position:absolute;left:10px;top:28px;font-size:7px"><span class="dot" style="width:5px;height:5px"></span>The Licensing Sage</div>
      <div class="card-contact" style="top:42px">
        <div class="name">Tessa Corvane</div>
        <div>President</div>
        <div>P.O. Box 518 Midway, Utah 84071</div>
        <div>Tessa@TheLicensingSage.example</div>
        <div>TheLicensingSage.example</div>
      </div>
      <svg class="wave" width="196" height="16" viewBox="0 0 196 16" preserveAspectRatio="none">
        <path d="M0 7 Q98 0 196 5" fill="none" stroke="var(--orange)" stroke-width="1.2"/>
        <path d="M0 10 Q98 3 196 8 L196 16 L0 16Z" fill="var(--green)"/>
      </svg>
    </div>
  </div>

  <!-- Business card back -->
  <div class="wrap" style="left:984px;top:29px;width:192px;height:103px">
    <div class="piece-label">Business Card (Back)</div>
    <div class="piece card-back" style="inset:0">
      <p>Let us share the wisdom we have acquired from running franchises and selling hundreds of them. Our service is always free to you.</p>
      <div class="brand" style="position:absolute;right:10px;bottom:16px;font-size:6px;color:#fff"><span class="dot" style="width:5px;height:5px"></span>The Licensing Sage</div>
    </div>
  </div>

  <!-- Envelope front -->
  <div class="wrap" style="left:775px;top:156px;width:401px;height:180px">
    <div class="piece-label">Envelope (Front)</div>
    <div class="piece" style="inset:0">
      <div class="brand" style="position:absolute;left:16px;top:18px;font-size:12px"><span class="dot" style="width:8px;height:8px"></span>The Licensing Sage</div>
      <div class="tagline" style="position:absolute;left:30px;top:38px">P.O. Box 518 Midway, Utah 84071</div>
      <svg class="wave" width="401" height="50" viewBox="0 0 401 50" preserveAspectRatio="none">
        <path d="M0 14 Q200 0 401 22" fill="none" stroke="var(--orange)" stroke-width="1.5"/>
        <path d="M0 18 Q200 4 401 26 L401 50 L0 50Z" fill="var(--green)"/>
      </svg>
    </div>
  </div>

  <!-- Envelope back -->
  <div class="wrap" style="left:775px;top:355px;width:401px;height:178px">
    <div class="piece-label">Envelope (Back)</div>
    <div class="piece" style="inset:0">
      <svg width="401" height="178" viewBox="0 0 401 178" style="position:absolute;left:0;top:0">
        <path d="M0 0 L401 0 L401 30 L215 110 Q200 116 186 110 L0 30Z" fill="var(--green)"/>
        <path d="M0 30 L186 110 Q200 116 215 110 L401 30" fill="none" stroke="var(--orange)" stroke-width="1.5"/>
        <path d="M0 178 L170 100 M401 178 L231 100" stroke="#e2e2e2" stroke-width="1"/>
        <circle cx="200" cy="62" r="14" fill="#fff"/>
      </svg>
    </div>
  </div>

</div>
</body>
</html>
```